Accident Law Firm Billboard Bold Easy to See Car Accidents

We need a billboard design that can catch attention in a very crowed Car Accident lawyer market. We wish to feature the phone number (652) 318-4470 as the focus of the Bill Board. We are trying to get the phone number recognized and remembered by drivers. The law firm name is not as crucial to remember.
Basically, It's CAR ACCIDENT? Then (652) 318-4470. We are not married to any specific color scheme but it has to POP and catch attention.
So the Crucial elements are as follows:
1. Phone number (652) 318-4470
2. Words CAR ACCIDENT?
3. Firm Logo in lower portion or where appropriate. Firm Logo to be provided
4. We may want to try a Day Glow orange color, with White and Black added. An example of the color scheme shall be provided.
5. Possible "Catch Phrase" to be used, "It's Time Call 9"
Target Market(s)
Orlando Florida Car Accident victims
Industry/Entity Type
Law Firm
Requirements
Must have
- Easy to see phone number (652) 318-4470
- Catch attention
Nice to have
- I would like to have the sign visible in bright sunlight and it not too hard to immediately know what phone number is for
Should not have
- too many words
- No bold enough
- confusing fonts
- Unclear fonts

```html
<!DOCTYPE html>
<html lang="en">
<head>
<meta charset="utf-8">
<title>Car Accident Billboard</title>
<link rel="stylesheet" href="https://fonts.googleapis.com/css2?family=Ubuntu:wght@700&display=swap">
<style>
  :root {
    --dayglow-orange: #e04010;
    --panel-white: #ffffff;
    --panel-black: #000000;
    --ink-black: #000000;
    --ink-white: #ffffff;
    --lane-white: #ffffff;
    --headline-shadow: rgba(40, 20, 10, 0.55);
  }

  * { margin: 0; padding: 0; box-sizing: border-box; }

  html, body {
    width: 1200px;
    height: 440px;
    overflow: hidden;
    background: var(--dayglow-orange);
  }

  .billboard {
    position: relative;
    width: 1200px;
    height: 440px;
    background: var(--dayglow-orange);
    font-family: "Ubuntu", "Arial Black", sans-serif;
    font-weight: 700;
    overflow: hidden;
  }

  .headline-panel {
    position: absolute;
    left: 0;
    top: 46px;
    width: 950px;
    height: 138px;
    background: var(--panel-white);
    border-radius: 0 40px 40px 0;
    display: flex;
    align-items: center;
  }

  .headline {
    margin-left: 140px;
    font-size: 88px;
    line-height: 1;
    letter-spacing: -0.5px;
    color: var(--ink-black);
    text-shadow: 4px 5px 3px var(--headline-shadow);
    white-space: nowrap;
    padding-top: 6px;
  }

  .lane-divider {
    position: absolute;
    left: 8px;
    top: 216px;
    width: 1192px;
    height: 14px;
    background: repeating-linear-gradient(
      to right,
      var(--lane-white) 0 56px,
      transparent 56px 80px
    );
  }

  .phone-panel {
    position: absolute;
    left: 218px;
    top: 260px;
    width: 1000px;
    height: 136px;
    background: var(--panel-black);
    border-radius: 40px 0 0 40px;
    display: flex;
    align-items: center;
  }

  .phone-cta {
    margin-left: 102px;
    font-size: 84px;
    line-height: 1;
    letter-spacing: -0.5px;
    color: var(--ink-white);
    white-space: nowrap;
    padding-top: 4px;
  }
</style>
</head>
<body>
  <main class="billboard">
    <div class="headline-panel">
      <h1 class="headline">CAR ACCIDENT ?</h1>
    </div>

    <div class="lane-divider" aria-hidden="true"></div>

    <div class="phone-panel">
      <p class="phone-cta">CALL (652) 318-4470</p>
    </div>
  </main>
</body>
</html>
```